Car rental website design for a UAE car rental company

This project is about creating a new website design for a car rental company located in Dubai (United Arab Emirates), I opened the same project a few months ago but I didn't receive a lot of appealing entries so I closed it but this time I am marking the project as guaranteed to avoid such situation again, if you have already provided a design before then please re-submit again on this project so that it is considered while reviewing all the designs

A few important things:

1- We need a simple non-complex design
2- The final deliverable would be 2 screens (PSD, JPEG ... etc), the first screen is for the home page and the second screen is for an internal page
3- The home page must have a section that end users can use to rent a car online directly from the home page instead of going into some inner pages
4- The current website is very old and not very appealing so avoid creating a similar design (www.quarvin-drive.example)
5- The name is Quarvin but the company rents normal cars (no Limousin cars will be rented) so avoid adding any fancy cars in the images/graphics used in the design, just normal end users cars
6- The expected pages would be: home, About us, Our team, Strategy, Contact us and links to social media pages
7- The attachments include the company's logo and some screens from other car rental companies that provide online rentals/payments

If you have any questions please feel free to ask and please note that we will need the designs urgently

Thanks

Target Market(s)

Dubai - United Arab Emirates

Industry/Entity Type

It Company

Number of Pages Required

2 page

Font styles to use
Sans Serif

Requirements
Must have
• Check the project details
Nice to have
Should not have

```html
<!DOCTYPE html>
<html lang="en">
<head>
<meta charset="utf-8">
<title>Quarvin – Rent A Car</title>
<link href="https://fonts.googleapis.com/css2?family=Roboto:wght@300;400;500;700&family=Open+Sans:wght@300;400&display=swap" rel="stylesheet">
<style>
:root{
  --brand:#a3082c;
  --brand-dark:#7e0620;
  --ink:#222;
  --muted:#555;
  --soft:#e6e7e8;
  --line:#d8d8d8;
  --white:#fff;
  --dark:#2b2e33;
}
*{box-sizing:border-box;margin:0;padding:0}
html,body{width:978px;height:1200px;overflow:hidden;background:var(--white)}
body{position:relative;font-family:'Roboto',Arial,sans-serif;color:var(--ink)}
.abs{position:absolute}

/* header */
.site-header{position:absolute;left:0;top:0;width:978px;height:88px}
.brand{left:112px;top:14px;display:flex;align-items:center;gap:8px}
.brand-mark{width:30px;height:30px;background:var(--brand)}
.brand-name{font-size:22px;font-weight:500;color:var(--brand)}
.phone{right:116px;top:12px;display:flex;align-items:center;gap:8px;font-size:21px;font-weight:500;color:#333}
.account{right:116px;top:48px;display:flex;gap:16px;font-size:15px;color:#333}
.account span{display:flex;align-items:center;gap:5px}

/* nav */
.main-nav{position:absolute;left:0;top:88px;width:978px;height:36px;background:var(--brand);display:flex;padding-left:113px}
.main-nav a{color:var(--white);text-decoration:none;font-size:15px;font-weight:500;line-height:36px;padding:0 20px;position:relative}
.main-nav a+a::before{content:"";position:absolute;left:0;top:8px;height:22px;width:1px;background:rgba(255,255,255,.8)}
.main-nav a:first-child{padding-left:21px;padding-right:29px}
.main-nav a:nth-child(2){padding-right:30px}
.main-nav a:nth-child(3){padding-right:21px}

/* hero */
.hero{position:absolute;left:0;top:124px;width:978px;height:298px;background:linear-gradient(90deg,#eaecee,#f3f4f5 60%,#e3e5e7);overflow:hidden}
.hero-photo{position:absolute;right:0;top:0;width:422px;height:298px;background:linear-gradient(160deg,#7d8b93 0%,#54626b 45%,#23282d 100%);clip-path:polygon(40px 0,100% 0,100% 100%,34px 100%,0 50%)}
.hero-arrow{position:absolute;top:132px;width:29px;height:34px;background:#9aa0a6;display:flex;align-items:center;justify-content:center}
.search-box{position:absolute;left:114px;top:58px;width:407px;height:182px;background:var(--white);padding:10px 12px}
.search-box h1{font-family:'Open Sans',sans-serif;font-weight:400;font-size:22px;color:#666;margin-bottom:6px}
.field-label{font-size:9px;color:#777;position:absolute}
.field{position:absolute;height:24px;border:1px solid #ccc;font-size:7px;color:#999;display:flex;align-items:center;gap:6px;padding-left:8px}
.btn-search{position:absolute;left:12px;top:148px;width:89px;height:24px;background:var(--brand);color:var(--white);font-size:10px;display:flex;align-items:center;justify-content:center}

/* features */
.intro{left:115px;top:462px;width:240px}
.intro h2{font-size:15px;font-weight:500;line-height:21px;margin-bottom:10px}
.intro p,.feature p{font-size:10.5px;line-height:13.5px;color:#444}
.learn{left:115px;top:604px;display:flex;align-items:center;gap:8px;font-size:13px;font-weight:500}
.feature{width:225px}
.feature h3{font-size:13px;font-weight:500;display:flex;align-items:center;gap:10px;margin-bottom:12px}

/* offers */
.offers{position:absolute;left:0;top:660px;width:978px;height:403px;background:var(--soft)}
.offers-kicker{position:absolute;width:100%;top:24px;text-align:center;font-size:16px;color:#333}
.offers-title{position:absolute;width:100%;top:44px;text-align:center;font-size:23px;font-weight:700;color:var(--brand)}
.tabs{position:absolute;left:274px;top:90px;width:432px;height:32px}
.tab-label{position:absolute;top:90px;height:32px;line-height:32px;font-size:10px;font-weight:500;color:var(--white);text-align:center}
.car-card{position:absolute;top:153px;width:210px;height:217px;background:var(--white)}
.car-photo{height:124px}
.car-name{text-align:center;font-size:9px;font-weight:700;margin-top:10px}
.car-price{text-align:center;font-size:8.5px;color:#666;margin-top:4px}
.rent-btn{display:block;margin:8px auto 0;width:68px;height:23px;background:var(--dark);color:var(--white);font-size:8px;text-align:center;line-height:23px}
.rent-btn.active{background:var(--brand)}
.specs{position:absolute;bottom:0;left:0;width:100%;height:24px;border-top:1px solid #e5e5e5;display:flex}
.specs span{flex:1;font-size:7px;color:#666;display:flex;align-items:center;justify-content:center;gap:3px;border-left:1px solid #e5e5e5}
.specs span:first-child{border-left:0}
.specs i{width:6px;height:5px;background:#999;border-radius:1px;display:inline-block}
.offer-arrow{position:absolute;top:218px}

/* signup */
.signup-title{left:115px;top:1098px;font-size:19.5px;font-weight:700;color:#222}
.signup-sub{left:115px;top:1124px;font-size:10.5px;color:#d4d4d4;font-weight:500}
.signup-form{left:430px;top:1096px;width:241px;height:41px;border:2px solid var(--brand);background:var(--white)}
.signup-form span{position:absolute;left:20px;top:12px;font-size:9px;color:#888}
.signup-form b{position:absolute;right:10px;top:9px;width:44px;height:21px;border:1px solid #bbb;font-size:11px;line-height:19px;text-align:center;color:#333;font-weight:700}
.social{position:absolute;top:1099px;width:42px;height:36px}
.site-footer{position:absolute;left:0;top:1166px;width:978px;height:34px;background:var(--brand);color:var(--white);font-size:10px;text-align:center;line-height:34px}
</style>
</head>
<body>

<header class="site-header">
  <div class="abs brand"><span class="brand-mark"></span><span class="brand-name">Quarvin</span></div>
  <div class="abs phone">
    <svg width="24" height="24" viewBox="0 0 24 24"><circle cx="12" cy="12" r="11" fill="none" stroke="#a3082c" stroke-width="1.5"/><path d="M8 6.5l2 0 1 3-1.4 1.2a7 7 0 0 0 3.7 3.7L14.5 13l3 1v2a1.5 1.5 0 0 1-1.6 1.5A10 10 0 0 1 6.5 8.1 1.5 1.5 0 0 1 8 6.5z" fill="#a3082c"/></svg>
    (555) 013-2290
  </div>
  <div class="abs account">
    <span><svg width="11" height="13" viewBox="0 0 11 13"><rect x="1" y="5.5" width="9" height="7" fill="#888"/><path d="M3 5.5V3.5a2.5 2.5 0 0 1 5 0v2" stroke="#888" stroke-width="1.4" fill="none"/></svg>Login</span>
    <span><svg width="14" height="14" viewBox="0 0 14 14"><circle cx="7" cy="7" r="6" fill="none" stroke="#888" stroke-width="1.2"/><circle cx="7" cy="5.5" r="2" fill="#888"/><path d="M3.5 11a3.5 3 0 0 1 7 0" fill="#888"/></svg>SignUp</span>
  </div>
</header>

<nav class="main-nav">
  <a href="#">Home</a><a href="#">About Us</a><a href="#">Our Team</a><a href="#">Strategy</a><a href="#">Contact Us</a>
</nav>

<section class="hero">
  <div class="hero-photo" role="img" aria-label="Red compact car parked in a concrete showroom"></div>
  <div class="hero-arrow" style="left:0"><svg width="10" height="16" viewBox="0 0 10 16"><path d="M8 2L2 8l6 6" stroke="#fff" stroke-width="2" fill="none"/></svg></div>
  <div class="hero-arrow" style="right:0;background:#3a3f44"><svg width="10" height="16" viewBox="0 0 10 16"><path d="M2 2l6 6-6 6" stroke="#fff" stroke-width="2" fill="none"/></svg></div>

  <form class="search-box">
    <h1>Search for Rental Cars</h1>
    <span class="field-label" style="left:12px;top:40px">Pick-up From</span>
    <span class="field-label" style="left:213px;top:40px">Drop-off To</span>
    <div class="field" style="left:12px;top:54px;width:184px"><svg width="7" height="10" viewBox="0 0 7 10"><path d="M3.5 0A3.5 3.5 0 0 0 0 3.5C0 6 3.5 10 3.5 10S7 6 7 3.5A3.5 3.5 0 0 0 3.5 0z" fill="#aaa"/></svg>City, Airport or U.S. Zip Code</div>
    <div class="field" style="left:213px;top:54px;width:184px"><svg width="7" height="10" viewBox="0 0 7 10"><path d="M3.5 0A3.5 3.5 0 0 0 0 3.5C0 6 3.5 10 3.5 10S7 6 7 3.5A3.5 3.5 0 0 0 3.5 0z" fill="#aaa"/></svg>City, Airport or U.S. Zip Code</div>
    <span class="field-label" style="left:12px;top:96px">Pick-up Date</span>
    <span class="field-label" style="left:113px;top:96px">Pick-up Time</span>
    <span class="field-label" style="left:213px;top:96px">Drop-off Date</span>
    <span class="field-label" style="left:314px;top:96px">Drop-off Time</span>
    <div class="field" style="left:12px;top:111px;width:84px"><svg width="9" height="9"><rect width="9" height="9" fill="#bbb"/></svg>mm/dd/yyyy</div>
    <div class="field" style="left:113px;top:111px;width:84px"><svg width="9" height="9"><circle cx="4.5" cy="4.5" r="4" fill="none" stroke="#aaa"/></svg>3:00 PM</div>
    <div class="field" style="left:213px;top:111px;width:84px"><svg width="9" height="9"><rect width="9" height="9" fill="#bbb"/></svg>mm/dd/yyyy</div>
    <div class="field" style="left:314px;top:111px;width:84px"><svg width="9" height="9"><circle cx="4.5" cy="4.5" r="4" fill="none" stroke="#aaa"/></svg>3:00 PM</div>
    <div class="btn-search">Search for Cars</div>
  </form>
</section>

<section>
  <div class="abs intro">
    <h2>We are leading car rental agency with 300,000 Happy Customers.</h2>
    <p>Morbi orci ante,consectetur id vestibulum quis,suscipit eu eros.Duis non egestas dolor. Duis non volutpat leo.Aliquam nisi eros,accu msan non gravida vitae,ultrices eu eros.Phasell sagittis mattis tristique.</p>
  </div>
  <div class="abs learn"><svg width="18" height="18" viewBox="0 0 18 18"><circle cx="9" cy="9" r="8" fill="none" stroke="#a3082c" stroke-width="1.5"/><path d="M7 5l4 4-4 4" stroke="#a3082c" stroke-width="2" fill="none"/></svg>LEARN MORE</div>

  <div class="abs feature" style="left:380px;top:464px">
    <h3><svg width="11" height="11"><path d="M0 0h6l5 5-6 6-5-5z" fill="#a3082c"/></svg>Special low rates on car booking</h3>
    <p>Nunc ut nibh enim,id dapibus quam.Mauris id est at diam rutrum ultricies.Vivamus et dolor velit.Nam congue blandit nulla sed tincidunt.</p>
  </div>
  <div class="abs feature" style="left:638px;top:464px">
    <h3><svg width="12" height="12"><rect x="1" y="1" width="10" height="10" fill="none" stroke="#a3082c" stroke-width="1.5"/><path d="M4 8l6-6" stroke="#a3082c" stroke-width="2"/></svg>Manage your booking online</h3>
    <p>Aliquam erat volutpat.Pellentesque habitant morbi tristique senectus et netus et malesuada fames ac turpis egestas.</p>
  </div>
  <div class="abs feature" style="left:380px;top:554px">
    <h3><svg width="12" height="12"><circle cx="6" cy="6" r="5" fill="none" stroke="#a3082c" stroke-width="2"/><circle cx="6" cy="6" r="2" fill="#a3082c"/></svg>Dedicated customer support</h3>
    <p>Praesent tempus egestas blandit. Nunc euismo volutpat ultrices.Nam fermentum nibh eget mi vehicula dictum.</p>
  </div>
  <div class="abs feature" style="left:638px;top:554px">
    <h3><svg width="12" height="12"><circle cx="6" cy="6" r="5" fill="none" stroke="#a3082c" stroke-width="1.5"/><path d="M6 3v3h2" stroke="#a3082c" stroke-width="1.5" fill="none"/></svg>You are guaranteed a car</h3>
    <p>Donec vitae orci metus,et viverra ipsum.Curabit tristique tristique lacinia.Sed sagittis placerat vestibulum.</p>
  </div>
</section>

<section class="offers">
  <div class="offers-kicker">What a Kind Of Car You Want</div>
  <div class="offers-title">GREAT RENTAL OFFERS FOR YOU</div>
  <svg class="tabs" viewBox="0 0 432 32" width="432" height="32">
    <path d="M16 0H137V32H16L0 16z" fill="#2b2e33"/>
    <rect x="137" y="0" width="157" height="32" fill="#a3082c"/>
    <path d="M294 0H416L432 16 416 32H294z" fill="#2b2e33"/>
  </svg>
  <span class="tab-label" style="left:290px;width:121px">BEST OFFERS</span>
  <span class="tab-label" style="left:411px;width:157px">POPULAR CARS</span>
  <span class="tab-label" style="left:568px;width:122px">ECONOMIC CARS</span>

  <svg class="offer-arrow" style="left:96px" width="36" height="36" viewBox="0 0 36 36"><path d="M18 2L34 18 18 34 2 18z" fill="none" stroke="#222" stroke-width="1.6"/><path d="M20 12l-6 6 6 6" stroke="#222" stroke-width="1.8" fill="none"/></svg>
  <svg class="offer-arrow" style="left:844px" width="36" height="36" viewBox="0 0 36 36"><path d="M18 2L34 18 18 34 2 18z" fill="none" stroke="#222" stroke-width="1.6"/><path d="M16 12l6 6-6 6" stroke="#222" stroke-width="1.8" fill="none"/></svg>

  <article class="car-card" style="left:154px">
    <div class="car-photo" role="img" aria-label="Silver sedan by a waterfront at dusk" style="background:linear-gradient(180deg,#6f8aa3,#3d4a57 70%,#222a31)"></div>
    <div class="car-name">ARDENT SEDAN 2.0 D</div>
    <div class="car-price">Start from 39$/per a day</div>
    <span class="rent-btn active">RENT IT</span>
    <div class="specs"><span><i></i>2011</span><span><i></i>Diesel</span><span><i></i>Auto</span><span><i></i>25000</span></div>
  </article>
  <article class="car-card" style="left:380px">
    <div class="car-photo" role="img" aria-label="Red hatchback in front of a glass building" style="background:linear-gradient(180deg,#9fb4c6,#7a8d9c 55%,#5b6066)"></div>
    <div class="car-name">ARDENT CITY 2.0 D</div>
    <div class="car-price">Start from 39$/per a day</div>
    <span class="rent-btn">RENT IT</span>
    <div class="specs"><span><i></i>2013</span><span><i></i>Diesel</span><span><i></i>Auto</span><span><i></i>25000</span></div>
  </article>
  <article class="car-card" style="left:606px">
    <div class="car-photo" role="img" aria-label="Grey hatchback on a city street in the evening" style="background:linear-gradient(180deg,#24466e,#4b5560 60%,#2c2f33)"></div>
    <div class="car-name">ARDENT HATCH 2.0 D</div>
    <div class="car-price">Start from 39$/per a day</div>
    <span class="rent-btn">RENT IT</span>
    <div class="specs"><span><i></i>2014</span><span><i></i>Diesel</span><span><i></i>Auto</span><span><i></i>25000</span></div>
  </article>
</section>

<section>
  <div class="abs signup-title">SIGN UP FOR AMAZING OFFERS</div>
  <div class="abs signup-sub">EXCLUSIVE ACCESS FOR OFFERS AND PROMOTIONS</div>
  <div class="abs signup-form"><span>Enter your Email Address</span><b>SEND</b></div>
  <span class="social" style="left:718px;background:#2f9ad6" aria-label="Social network one"></span>
  <span class="social" style="left:767px;background:#d33a2c" aria-label="Social network two"></span>
  <span class="social" style="left:816px;background:#3b5a9a" aria-label="Social network three"></span>
</section>

<footer class="site-footer">©Copyright 2015, Quarvin. All rights reserved.</footer>

</body>
</html>
```